Web Design For Metal Recycling Company

We are a scrap and recycling company dealing mainly in scrap metal base in Singapore. We deal in both domestic market and international market. Currently we are still unsure if we want to have a "lively" or "professional" company image so we will leave it to the designer to deem what is good.

We wish for a website to be able to "Retain" the interest of new visitor and at the same time able to give enough information for new and existing customer. We would also wish for design that will get the visitor to "Engage" us.

The attached is the logo for the company and we would want to incorporate that into the website. Either of the logo is fine.

```html
<!DOCTYPE html>
<html lang="en">
<head>
<meta charset="utf-8">
<title>Tan Keng Metals – Home</title>
<link rel="stylesheet" href="https://fonts.googleapis.com/css2?family=Oxygen:wght@400;700&family=Arimo:wght@400;700&family=Gelasio&display=swap">
<style>
  :root {
    --gold: #c9961c;
    --gold-dark: #8a6216;
    --gold-light: #f0cf79;
    --white: #ffffff;
    --ink: #2d2d2d;
    --ink-soft: #555555;
    --sidebar: rgba(40, 62, 84, 0.82);
    --panel: rgba(222, 236, 250, 0.86);
    --card: rgba(245, 245, 245, 0.92);
    --footer: rgba(40, 36, 30, 0.82);
    --orange: #f08a00;
  }
  * { box-sizing: border-box; margin: 0; padding: 0; }
  html, body { width: 1200px; height: 800px; overflow: hidden; }
  body { font-family: "Oxygen", sans-serif; position: relative; }

  .scene-photo {
    position: absolute; inset: 0;
    background: linear-gradient(to bottom,
      #5c9fdc 0%, #8cc0ee 38%, #5c6a4c 46%, #3f4a33 52%,
      #8a8276 60%, #a69a86 75%, #b8a68a 100%);
  }

  .sidebar {
    position: absolute; left: 149px; top: 0; width: 211px; height: 690px;
    background: linear-gradient(to bottom, var(--sidebar) 70%, rgba(40,62,84,0) 100%);
  }
  .brand { position: absolute; left: 0; top: 12px; width: 211px; text-align: center; }
  .brand-mark {
    width: 104px; height: 104px; margin: 0 auto;
    border: 6px solid var(--gold);
  }
  .brand-name {
    margin-top: 14px; color: var(--gold); font-weight: 700;
    font-size: 19px; letter-spacing: 1px;
  }

  .main-nav { position: absolute; left: 21px; top: 220px; list-style: none; }
  .main-nav li { height: 38px; line-height: 20px; font-size: 14px; font-weight: 700; color: var(--white); }
  .main-nav li.active { color: var(--gold-light); }

  .contact { position: absolute; left: 11px; top: 512px; color: var(--white); }
  .contact-label { display: flex; align-items: center; gap: 10px; font-weight: 700; font-size: 14px; height: 20px; }
  .contact-value { font-size: 15px; margin-top: 4px; margin-bottom: 13px; letter-spacing: 0.3px; }
  .social { display: flex; gap: 8px; margin-left: 5px; margin-top: 6px; }
  .social span { width: 28px; height: 28px; border-radius: 50%; background: #b59a6a; border: 2px solid #efe6d4; }

  .top-nav {
    position: absolute; right: 158px; top: 20px;
    font-family: "Arimo", sans-serif; font-weight: 700; font-size: 14px; color: var(--ink);
    word-spacing: 2px;
  }
  .top-nav .sep { margin: 0 10px; }

  .intro {
    position: absolute; left: 388px; top: 96px; width: 664px; height: 237px;
    background: var(--panel); border-radius: 4px; padding: 30px 25px 0 25px;
  }
  .intro h1 { font-family: "Gelasio", serif; font-weight: 400; font-size: 28px; line-height: 34px; color: var(--ink); }
  .intro p { font-family: "Arimo", sans-serif; font-size: 15px; line-height: 24px; color: #333; margin-top: 16px; }
  .read-more { font-size: 12px; color: var(--ink); display: inline-flex; align-items: center; gap: 3px; }
  .intro .read-more { position: absolute; right: 50px; bottom: 24px; }
  .dot { width: 10px; height: 10px; border-radius: 50%; background: var(--orange); position: relative; }
  .dot::after { content: ""; position: absolute; left: 3px; top: 3px; width: 3px; height: 3px;
    border-top: 1.5px solid #fff; border-right: 1.5px solid #fff; transform: rotate(45deg); }

  .feature {
    position: absolute; top: 472px; width: 205px; height: 200px;
    background: var(--card); border-radius: 3px; text-align: center; padding-top: 12px;
  }
  .feature-icon {
    width: 76px; height: 74px; margin: 0 auto;
    border: 3px solid var(--gold);
    background: linear-gradient(135deg, #f4f0e6, #e4d6b4);
  }
  .feature h2 { font-weight: 400; font-size: 18px; color: var(--gold-dark); margin-top: 10px; letter-spacing: 0.3px; }
  .feature p { font-size: 12px; line-height: 15.5px; color: var(--ink-soft); margin: 5px 8px 0; }
  .feature .read-more { margin-top: 9px; }

  .site-footer {
    position: absolute; left: 0; top: 743px; width: 1200px; height: 28px;
    background: var(--footer); color: var(--white); font-size: 12px;
    text-align: right; padding-right: 152px; line-height: 28px;
  }
</style>
</head>
<body>
  <div class="scene-photo" role="img" aria-label="Scrap metal yard with an excavator, containers and trees under a blue sky"></div>

  <aside class="sidebar">
    <div class="brand">
      <div class="brand-mark"></div>
      <div class="brand-name">TAN KENG METALS</div>
    </div>
    <ul class="main-nav">
      <li class="active">HOME</li>
      <li>Products &amp; Services</li>
      <li>Health &amp; Saftey</li>
      <li>Resources</li>
      <li>About Us</li>
      <li>Location</li>
      <li>Contact Us</li>
    </ul>
    <div class="contact">
      <div class="contact-label">
        <svg width="16" height="18" viewBox="0 0 16 18"><path d="M3 1 L6 1 L7 5 L5 7 Q7 11 10 13 L12 11 L15 12 L15 15 Q13 17 10 16 Q3 12 1 5 Q1 2 3 1Z" fill="#f2c200"/></svg>
        Call
      </div>
      <div class="contact-value">123-55501234</div>
      <div class="contact-label">
        <svg width="18" height="12" viewBox="0 0 18 12"><rect x="0" y="0" width="18" height="12" fill="#f2c200"/><path d="M0 0 L9 7 L18 0" fill="none" stroke="#3b4d5e" stroke-width="1.5"/></svg>
        Mail
      </div>
      <div class="contact-value">info@tankengmetals.com</div>
      <div class="social"><span></span><span></span><span></span></div>
    </div>
  </aside>

  <nav class="top-nav">Buying<span class="sep">|</span>Selling<span class="sep">|</span>Scrap Management<span class="sep">|</span>Recycling</nav>

  <section class="intro">
    <h1>We deal in both Domestic market and International market.</h1>
    <p>Lorem ipsum dolor sit amet, consectetuer adipiscing elit, sed diam nonummy nibh euismod tincidunt ut laoreet dolore magna aliquam erat volutpat. Lorem ipsum dolor sit amet, consectetuer adipiscing elit, sed diam nonummy nibh euismod tincidunt ut laoreet dolore magna aliquam erat volutpat.</p>
    <span class="read-more">Read more <i class="dot"></i></span>
  </section>

  <article class="feature" style="left:394px">
    <div class="feature-icon" role="img" aria-label="Light bulb icon"></div>
    <h2>NEWS &amp; EVENTS</h2>
    <p>Duis autem vel eum iriure dolor in hendrerit in vulptate velit olestie consequat, vel illum dolore eu</p>
    <span class="read-more">Read more <i class="dot"></i></span>
  </article>
  <article class="feature" style="left:618px">
    <div class="feature-icon" role="img" aria-label="Two hands passing an item icon"></div>
    <h2>OUR COMMITMENT</h2>
    <p>Duis autem vel eum iriure dolor in hendrerit in vulptate velit olestie consequat, vel illum dolore eu</p>
    <span class="read-more">Read more <i class="dot"></i></span>
  </article>
  <article class="feature" style="left:841px">
    <div class="feature-icon" role="img" aria-label="Two person silhouettes icon"></div>
    <h2>OUR TEAM</h2>
    <p>Duis autem vel eum iriure dolor in hendrerit in vulptate velit olestie consequat, vel illum dolore eu</p>
    <span class="read-more">Read more <i class="dot"></i></span>
  </article>

  <footer class="site-footer">© 2014 Tankengmetals. All right reserved.</footer>
</body>
</html>
```